Education portal needs a new Email Creative Design

We could not decide on the creative earlier as we were unable to picture how will it look. Hence, we have added content so that we can choose the best design of all. Below is the content to be used for the email creative:
____________________________________
Did you know that 25% of all Americans have experienced at least one divorce?*
41% of first marriages end in divorce!!*

Over 1 million children are affected by divorce each year*

Become a Marriage and Family therapist - Achieve inner-happiness by helping individuals, families and couples resolve their struggles and enhance their lives.
Family Therapists are trained in various modes of therapy in order to prepare them for work with individuals, families, couples, and groups.

With proper training, you will be able to treat:
• Depression and other Affective Disorders
• Childhood Behavioral and Emotional Disorders
• Marital and Relationship Problems
• Conduct Disorder and Delinquency
• Substance Abuse
• Alcoholism
• Domestic Violence
• Severe Mental Illness
• Physical Illness

You could also qualify for financial aid* from the government to pursue this career..

Secure your life by earning upto $78,580* and attain peace of mind while helping others..

__________________________

These are the links to images we liked, but if you have something better, we would love to see them:
http://www.pictovale.example/photo/seperated-50317294?st=7kq2m81
http://www.pictovale.example/photo/domestic-violence-68204937?st=b4n9x52

We are an education portal offering options of schools, colleges, universities and courses to students and working professionals.

We are looking for an email creative which has great call-to-action; be creative and research more if you wish.
Incorporate call-to-action tabs, make it colorful, include pictures and content.
Also attached are industry standard creatives for your reference, let me know if you have any questions.
Updates

Please see new files uploaded

I have uploaded a new creative made by our design team. Follow similar guidelines

For those who have not submitted their designs, please send us soon. Thanks

We thought a content brief will do more justice to this design contest hence we have updated our brief with new content to create a newer design Please submit your designs soon. Thanks

Target Market(s)

25 to 50 years working professionals

Industry/Entity Type

Government

Font styles to use
Serif
Sans Serif
Decorative
Script

Requirements
Must have
• Call-to-action

```html
<!DOCTYPE html>
<html lang="en">
<head>
<meta charset="UTF-8">
<title>Marriage &amp; Family Therapist Careers</title>
<link href="https://fonts.googleapis.com/css2?family=Open+Sans:ital,wght@0,400;0,600;0,700;0,800;1,700&display=swap" rel="stylesheet">
<style>
:root{
  --red:#c1272d;
  --red-deep:#8e1a1f;
  --brown:#7a2a26;
  --ink:#3a3a3a;
  --muted:#6a6a6a;
  --white:#ffffff;
  --bar:#e4e4e4;
  --footer:#eeeeee;
}
*{margin:0;padding:0;box-sizing:border-box}
html,body{width:857px;height:1200px;overflow:hidden;background:var(--white)}
body{font-family:"Open Sans",Arial,sans-serif;color:var(--ink);position:relative}
.hero{position:absolute;left:0;top:0;width:857px;height:632px;overflow:hidden}
.hero-photo{position:absolute;inset:0;
  background:radial-gradient(ellipse 260px 230px at 700px 200px,#3a2a26 0%,#5b4640 45%,rgba(210,205,205,0) 75%),
             linear-gradient(160deg,#f4f2f2 0%,#e5e1e0 55%,#d6d0ce 100%)}
.hero-shapes{position:absolute;inset:0}
.headline{position:absolute;left:42px;top:262px;width:470px;text-transform:uppercase}
.headline .line{display:block;color:var(--white);font-weight:600;font-size:29px;letter-spacing:.3px;line-height:1.2}
.headline .accent{display:block;color:var(--red);font-weight:800;font-size:44px;line-height:1.1;margin:2px 0}
.call-cta{position:absolute;left:580px;top:450px;width:277px;height:100px;color:var(--white);padding:6px 0 0 22px;white-space:nowrap}
.call-cta .label{font-size:38px;font-weight:600;line-height:1.15}
.call-cta .number{font-size:28px;font-weight:400;line-height:1.3}
.intro{position:absolute;left:40px;top:648px;width:505px}
.intro .stat{color:var(--red);font-weight:700;font-size:13.5px;line-height:1.4}
.intro p{font-size:13px;line-height:1.45;margin-top:6px;color:var(--ink)}
.treat-bar{position:absolute;left:0;top:818px;width:560px;height:32px;background:var(--bar);padding:6px 0 0 40px;font-size:14px;font-weight:700;color:var(--ink)}
.treat-list{position:absolute;left:40px;top:858px;list-style:none;font-size:13.5px;line-height:22.5px;color:var(--ink)}
.treat-list li::before{content:"\2022";margin-right:6px}
.side-photo{position:absolute;left:560px;top:636px;width:297px;height:430px;overflow:hidden}
.side-photo .fill{position:absolute;inset:0;background:radial-gradient(ellipse 140px 160px at 170px 190px,#4a4a4a 0%,#2b2b2b 55%,#7d7d7d 100%)}
.side-photo svg{position:absolute;inset:0}
.earn{position:absolute;left:40px;top:1074px;width:800px;color:var(--red);font-weight:700;font-size:14.5px}
.footer{position:absolute;left:0;top:1104px;width:857px;height:96px;background:var(--footer)}
.brand{position:absolute;left:40px;top:18px;font-size:50px;font-weight:400;color:#7b7b7b;letter-spacing:1px}
.contact{position:absolute;left:560px;top:16px;list-style:none;font-size:12.5px;color:var(--muted)}
.contact li{display:flex;align-items:center;height:21px}
.contact svg{width:12px;height:12px;margin-right:12px;flex:none}
</style>
</head>
<body>
<section class="hero">
  <div class="hero-photo" role="img" aria-label="Photo of a sad young woman resting her head on her arms, separated family theme"></div>
  <svg class="hero-shapes" width="857" height="632" viewBox="0 0 857 632">
    <polygon points="60,70 300,40 470,210 420,520 180,600 20,420" fill="#8a2e2a" opacity=".5"/>
    <polygon points="150,130 380,90 470,300 250,330" fill="#b0504a" opacity=".3"/>
    <polygon points="20,240 500,240 500,410 20,410" fill="#a0645e" opacity=".45"/>
    <polygon points="560,448 857,438 857,560 590,550" fill="#9e3531" opacity=".75"/>
  </svg>
  <h1 class="headline">
    <span class="line">Over 1 million children</span>
    <span class="accent">Are affected by</span>
    <span class="line">Divorce each year</span>
  </h1>
  <div class="call-cta">
    <div class="label">Call Now</div>
    <div class="number">1800 - 000 - 0000</div>
  </div>
</section>

<section class="intro">
  <div class="stat">Did you know that 25% of all Americans have experienced at least one divorce?<br>41% of first marriages end in divorce!!</div>
  <p>Become a Marriage and Family therapist - Achieve inner-happiness by helping individuals, families and couples resolve their struggles and enhance their lives.</p>
  <p>Family Therapists are trained in various modes of therapy in order to prepare them for work with individuals, families, couples, and groups.</p>
</section>

<div class="treat-bar">With proper training, you will be able to treat:</div>
<ul class="treat-list">
  <li>Depression and other Affective Disorders</li>
  <li>Childhood Behavioral and Emotional Disorders</li>
  <li>Marital and Relationship Problems</li>
  <li>Conduct Disorder and Delinquency</li>
  <li>Substance Abuse</li>
  <li>Alcoholism</li>
  <li>Domestic Violence</li>
  <li>Severe Mental Illness</li>
  <li>Physical Illness</li>
</ul>

<div class="side-photo">
  <div class="fill" role="img" aria-label="Photo of a distressed woman covering her face, domestic violence theme"></div>
  <svg width="297" height="430" viewBox="0 0 297 430">
    <polygon points="0,0 110,0 40,130 0,110" fill="#8e1a1f" opacity=".9"/>
    <polygon points="0,110 40,130 0,260" fill="#5c1114" opacity=".85"/>
  </svg>
</div>

<p class="earn">Secure your life by earning upto $78,580* and attain peace of mind while helping others..</p>

<footer class="footer">
  <div class="brand">YOUR LOGO</div>
  <ul class="contact">
    <li><svg viewBox="0 0 12 12"><polygon points="2,1 11,6 2,11" fill="#c1272d"/></svg>(201) 000 - 0000</li>
    <li><svg viewBox="0 0 12 12"><polygon points="2,1 11,6 2,11" fill="#c1272d"/></svg>www.yourweb.com</li>
    <li><svg viewBox="0 0 12 12"><polygon points="2,1 11,6 2,11" fill="#c1272d"/></svg>101, Linden Crest Drive, Norvale, NY 10012</li>
  </ul>
</footer>
</body>
</html>
```